Banner Ad for website hompage - Design Project

We need 4 banner ads for the homepage of a Rent a Car company based in dubai. We rent a wide range of cars but mainly deal in the affordable cars category. Our website colors are mainly red, white and black and I can send pictures of the website (attached) if you want something to compare possible design ideas with. The banners need to promote different messages and must be appealing to the end user. It must also use pictures of cars that exist in our fleet (Pls note: this is only if you are using cars in the banner ad)

The 4 banner ads needed are as follows:
1) should promote something along the lines of we have 20+ models available and reserve a car now (This banner should also have a reserve now button, not the actual button but it's design. The button will be made and coded by us)
2) should promote something along the lines of we offer personalised service and we look after each and every custoemr individually
3) we provide attractive rates based on daily, weekly, monthly and longer rental periods (should also incorporate a reserve now message)
4) Like us on quorvia and follow us on social media for additional offers and discounts (would like for this to have a like button design implemented in it which will be linked to quorvia.)

Also please not the picture file size is 940pixels by 400pixels

Finally: I also need the psd files for the banners.

```html
<!DOCTYPE html>
<html lang="en">
<head>
<meta charset="utf-8">
<title>Rivaro Rent a Car – Offers and Discounts</title>
<link href="https://fonts.googleapis.com/css2?family=Open+Sans:wght@400;600;700&display=swap" rel="stylesheet">
<style>
  :root {
    --brand-red: #d4261c;
    --ink: #2b2b2b;
    --nav-ink: #444444;
    --header-top: #ffffff;
    --header-bottom: #ececec;
    --hero-light: #e6e6e6;
    --hero-dark: #a9a9a9;
    --tag-black: #0c0c0c;
    --social-one: #2f57a0;
    --social-one-dark: #26498a;
    --social-two: #2e9fd3;
    --social-two-dark: #2386b6;
    --social-three: #11689a;
    --social-three-dark: #0b5480;
    --social-four: #c61d1d;
    --social-four-dark: #a51414;
    --white: #ffffff;
  }
  * { box-sizing: border-box; margin: 0; padding: 0; }
  html, body { width: 1200px; height: 654px; overflow: hidden; background: var(--white); }
  body { font-family: "Open Sans", Arial, sans-serif; position: relative; }

  .site-header {
    position: absolute; left: 0; top: 0; width: 1200px; height: 141px;
    background: linear-gradient(var(--header-top), var(--header-bottom));
    border-bottom: 1px solid #cfcfcf;
  }
  .brand {
    position: absolute; left: 60px; top: 54px;
    font-size: 34px; font-weight: 700; color: var(--brand-red); letter-spacing: -0.5px;
  }
  .main-nav { position: absolute; top: 70px; left: 394px; display: flex; gap: 0; }
  .main-nav a {
    position: absolute; white-space: nowrap; text-decoration: none;
    font-size: 18px; font-weight: 600; color: var(--nav-ink); text-transform: uppercase;
  }
  .main-nav a.is-active { color: var(--brand-red); border-bottom: 2px solid var(--brand-red); padding-bottom: 1px; }

  .hero {
    position: absolute; left: 0; top: 141px; width: 1200px; height: 475px; overflow: hidden;
  }
  .hero-backdrop {
    position: absolute; left: 0; top: 0; width: 776px; height: 475px;
    background: radial-gradient(ellipse at 30% 35%, var(--hero-light), var(--hero-dark) 95%);
  }
  .hero-photo {
    position: absolute; left: 776px; top: 0; width: 424px; height: 475px;
    background:
      linear-gradient(180deg, #b9cde0 0%, #dfe7ee 30%, #5d6b55 42%, #7c7c78 55%, #575757 100%);
  }
  .hero-photo::after {
    content: ""; position: absolute; left: 0; top: 60px; width: 280px; height: 415px;
    background: linear-gradient(160deg, #e3231b, #b3120e 70%, #7d0a07);
    border-radius: 0 120px 40px 0;
  }
  .slide-tag {
    position: absolute; left: 62px; top: 103px; height: 52px; padding: 0 18px;
    background: var(--tag-black); color: var(--white);
    font-size: 20px; font-weight: 700; line-height: 52px;
  }
  .slide-tag::after {
    content: ""; position: absolute; left: 0; bottom: -12px;
    border-left: 12px solid var(--tag-black); border-bottom: 12px solid transparent;
  }
  .slide-title {
    position: absolute; left: 62px; top: 175px; white-space: nowrap;
    font-size: 44px; font-weight: 700; color: var(--ink); letter-spacing: -0.3px;
    text-shadow: 1px 1px 0 rgba(255,255,255,0.6);
  }
  .social-button {
    position: absolute; width: 268px; height: 52px; border-radius: 26px;
    border: 2px solid var(--white); box-shadow: 0 2px 4px rgba(0,0,0,0.25);
    color: var(--white); font-size: 19px; font-weight: 600;
    line-height: 48px; padding-left: 60px; white-space: nowrap;
  }
  .social-button .badge {
    position: absolute; left: -2px; top: -2px; width: 52px; height: 52px;
    border-radius: 50%; border: 2px solid var(--white);
  }
  .social-one { left: 62px; top: 263px; background: var(--social-one); }
  .social-one .badge { background: var(--social-one-dark); }
  .social-two { left: 346px; top: 263px; background: var(--social-two); }
  .social-two .badge { background: var(--social-two-dark); }
  .social-three { left: 62px; top: 335px; background: var(--social-three); }
  .social-three .badge { background: var(--social-three-dark); }
  .social-four { left: 346px; top: 335px; background: var(--social-four); }
  .social-four .badge { background: var(--social-four-dark); }

  .slider-arrow { position: absolute; top: 228px; }
  .slider-arrow.prev { left: 12px; }
  .slider-arrow.next { left: 1124px; }
  .slider-dots { position: absolute; left: 736px; top: 346px; }

  .hero-shadow {
    position: absolute; left: 0; top: 616px; width: 1200px; height: 38px;
    background: radial-gradient(ellipse 55% 100% at 50% 0%, rgba(0,0,0,0.22), rgba(0,0,0,0) 70%);
  }
</style>
</head>
<body>
  <header class="site-header">
    <div class="brand">Rivaro Rent a Car</div>
    <nav class="main-nav">
      <a href="#" style="left:0">Home</a>
      <a href="#" class="is-active" style="left:79px">About us</a>
      <a href="#" style="left:192px">Services &amp; Benefits</a>
      <a href="#" style="left:398px">Blog</a>
      <a href="#" style="left:473px">Contact us</a>
      <a href="#" style="left:608px">Resources</a>
    </nav>
  </header>

  <section class="hero">
    <div class="hero-backdrop"></div>
    <div class="hero-photo" role="img" aria-label="Photo of a red compact hatchback parked on a road with pine trees and mountains behind"></div>

    <div class="slide-tag">we provide</div>
    <h1 class="slide-title">Additional Offers and Discounts</h1>

    <a class="social-button social-one"><span class="badge"></span>Like us on quorvia</a>
    <a class="social-button social-two"><span class="badge"></span>Follow us on chirply</a>
    <a class="social-button social-three"><span class="badge"></span>Join us on Linkfold</a>
    <a class="social-button social-four"><span class="badge"></span>Find us on circlet</a>

    <svg class="slider-arrow prev" width="42" height="42" viewBox="0 0 42 42">
      <circle cx="21" cy="21" r="19" fill="rgba(255,255,255,0.15)" stroke="rgba(255,255,255,0.6)" stroke-width="2"/>
      <path d="M24 13 L16 21 L24 29" fill="none" stroke="rgba(255,255,255,0.7)" stroke-width="3"/>
    </svg>
    <svg class="slider-arrow next" width="42" height="42" viewBox="0 0 42 42">
      <circle cx="21" cy="21" r="19" fill="rgba(255,255,255,0.15)" stroke="rgba(255,255,255,0.6)" stroke-width="2"/>
      <path d="M18 13 L26 21 L18 29" fill="none" stroke="rgba(255,255,255,0.7)" stroke-width="3"/>
    </svg>

    <svg class="slider-dots" width="76" height="30" viewBox="0 0 76 30">
      <polygon points="8,0 76,0 68,30 0,30" fill="#ffffff"/>
      <circle cx="20" cy="15" r="4.5" fill="#d4261c"/>
      <circle cx="32" cy="15" r="4.5" fill="#d4261c"/>
      <circle cx="44" cy="15" r="4.5" fill="#d4261c"/>
      <circle cx="56" cy="15" r="4.5" fill="#111111"/>
    </svg>
  </section>

  <div class="hero-shadow"></div>
</body>
</html>
```